Private Investment Firm Needs PowerPoint Presentation Template

Design PowerPoint template, take Ridgeholm-submitted rough presentation draft, and drop it into new template. See attached Project Brief file for more detail.
Updates

Some decent designs have been submitted but they seem to lack the understanding of our target markets. I am hopeful that more time and feedback will result in better results.

Target Market(s)

Private company owners and intermediaries.

Font styles to use
Serif

Colors
3176b5

Requirements
Must have
• See attached Project Brief.
Nice to have
Should not have
• No B2C fluff--this is a B2B project.

```html
<!DOCTYPE html>
<html lang="en">
<head>
<meta charset="utf-8">
<title>Non-Control Capital Questionnaire</title>
<link href="https://fonts.googleapis.com/css2?family=Montserrat:wght@400;500;600;700&family=Libre+Baskerville:wght@400&display=swap" rel="stylesheet">
<style>
  :root {
    --brand-blue: #1269b3;
    --brand-blue-dark: #0a4a86;
    --ink: #3a3a3a;
    --white: #ffffff;
    --card-shadow: rgba(0, 0, 0, 0.13);
  }
  * { margin: 0; padding: 0; box-sizing: border-box; }
  html, body { width: 1200px; height: 676px; overflow: hidden; background: var(--white); }
  .slide {
    position: relative;
    width: 1200px; height: 676px;
    overflow: hidden;
    background: var(--white);
    font-family: "Montserrat", sans-serif;
  }
  .side-rail {
    position: absolute; left: 0; top: 0;
    width: 44px; height: 676px;
    background: var(--brand-blue);
  }
  .side-rail-right {
    position: absolute; right: 0; top: 0;
    width: 12px; height: 676px;
    background: var(--brand-blue);
  }
  .site-url {
    position: absolute;
    left: 22px; top: 336px;
    transform: translate(-50%, -50%) rotate(-90deg);
    white-space: nowrap;
    font-family: "Libre Baskerville", serif;
    font-size: 14px;
    color: var(--white);
    letter-spacing: 0.2px;
  }
  .page-number {
    position: absolute; right: 22px; top: 18px;
    font-family: "Libre Baskerville", serif;
    font-size: 16px;
    color: #222;
  }
  .slide-title {
    position: absolute; left: 86px; top: 81px;
    font-size: 29px; font-weight: 700;
    color: var(--brand-blue);
    letter-spacing: 0.4px;
  }
  .title-band {
    position: absolute; left: 44px; top: 136px;
    width: 1144px; height: 42px;
    background: var(--brand-blue);
    display: flex; align-items: center;
    padding-left: 42px;
  }
  .title-band h2 {
    font-size: 28.5px; font-weight: 700;
    color: var(--white);
    letter-spacing: 0.4px;
  }
  .subtitle {
    position: absolute; left: 86px; top: 186px;
    font-size: 16.6px; font-weight: 600;
    color: var(--brand-blue);
    letter-spacing: 0.2px;
  }
  .building-photo {
    position: absolute; left: 470px; top: 470px;
    width: 718px; height: 206px;
    background: linear-gradient(100deg, #ffffff 0%, #eef1f3 35%, #d7dde2 70%, #c7d0d6 100%);
  }
  .card {
    position: absolute; top: 300px;
    width: 344px; height: 218px;
    background: var(--white);
    border-radius: 60px 0 72px 0;
    box-shadow: 0 2px 14px var(--card-shadow);
  }
  .card-1 { left: 80px; }
  .card-2 { left: 446px; }
  .card-3 { left: 806px; }
  .badge {
    position: absolute; left: 198px; top: -18px;
    width: 128px; height: 87px;
  }
  .badge svg { position: absolute; left: 0; top: 0; width: 128px; height: 87px; }
  .badge-text {
    position: absolute; left: 18px; top: 0;
    width: 110px; text-align: center;
    color: var(--white);
  }
  .badge-label { display: block; font-size: 14.5px; font-weight: 500; margin-top: 9px; letter-spacing: 0.3px; }
  .badge-number { display: block; font-size: 36px; font-weight: 500; line-height: 1; margin-top: 1px; }
  .question {
    position: absolute; left: 37px; top: 28px;
    width: 178px;
    font-size: 15px; font-weight: 500;
    line-height: 15.7px;
    color: var(--brand-blue);
  }
  .card-2 .question { top: 22px; }
  .answers {
    position: absolute; left: 23px; top: 108px;
    width: 300px;
    list-style: none;
  }
  .card-3 .answers { top: 127px; }
  .answers li {
    position: relative;
    padding-left: 15px;
    font-size: 11.6px;
    line-height: 15.6px;
    color: var(--ink);
  }
  .answers li::before {
    content: "";
    position: absolute; left: 0; top: 4px;
    width: 7px; height: 8px;
    background: var(--brand-blue);
  }
  .answer-label { color: var(--brand-blue); }
  .brand {
    position: absolute; left: 68px; top: 612px;
    display: flex; align-items: center; gap: 8px;
  }
  .brand-dot {
    width: 36px; height: 36px;
    border-radius: 50%;
    background: var(--brand-blue);
  }
  .brand-name {
    font-family: "Libre Baskerville", serif;
    font-size: 19px;
    letter-spacing: 1.5px;
    color: var(--brand-blue-dark);
  }
</style>
</head>
<body>
<div class="slide">
  <div class="side-rail"></div>
  <div class="side-rail-right"></div>
  <div class="site-url">www.ridgeholmcapital.com</div>
  <div class="page-number">23</div>

  <h1 class="slide-title">NON-CONTROL CAPITAL QUESTIONNAIRE</h1>
  <div class="title-band"><h2>The Critical Questions to Ask of Any Prospective Non-Control Investor</h2></div>
  <p class="subtitle">Non-Control Capital is a specialty, so only those firms with deep experience investing it as a team should be considered</p>

  <div class="building-photo" role="img" aria-label="Photograph of a modern white building facade with vertical glass fins"></div>

  <section class="card card-1">
    <div class="badge">
      <svg viewBox="0 0 128 87" aria-hidden="true">
        <polygon points="0,18 18,0 18,18" fill="var(--brand-blue-dark)"/>
        <polygon points="18,0 128,0 128,87 18,80" fill="var(--brand-blue)"/>
      </svg>
      <div class="badge-text"><span class="badge-label">QUESTION</span><span class="badge-number">01</span></div>
    </div>
    <h3 class="question">How many years has the firm been investing Non-Control Capital?</h3>
    <ul class="answers">
      <li><span class="answer-label">Best Answer:</span> 5+ years investing as a team within the current firm.</li>
      <li>Indicates comfort and experience evaluating and making NCC investments with each other and increases likelihood of close.</li>
    </ul>
  </section>

  <section class="card card-2">
    <div class="badge">
      <svg viewBox="0 0 128 87" aria-hidden="true">
        <polygon points="0,18 18,0 18,18" fill="var(--brand-blue-dark)"/>
        <polygon points="18,0 128,0 128,87 18,80" fill="var(--brand-blue)"/>
      </svg>
      <div class="badge-text"><span class="badge-label">QUESTION</span><span class="badge-number">02</span></div>
    </div>
    <h3 class="question">How may fully-invested Non-Control Capital funds in the firm’s history?</h3>
    <ul class="answers">
      <li><span class="answer-label">Best Answer:</span> 2+ fully-invested funds.</li>
      <li>Indicates experience and ability to close deals with the current regime—those firms without it may only be testing the waters and not have a long-term commitment to NCC investing.</li>
    </ul>
  </section>

  <section class="card card-3">
    <div class="badge">
      <svg viewBox="0 0 128 87" aria-hidden="true">
        <polygon points="0,18 18,0 18,18" fill="var(--brand-blue-dark)"/>
        <polygon points="18,0 128,0 128,87 18,80" fill="var(--brand-blue)"/>
      </svg>
      <div class="badge-text"><span class="badge-label">QUESTION</span><span class="badge-number">03</span></div>
    </div>
    <h3 class="question">What percentage of the firm’s voting investment committee are full-time Non-Control Capital investors?</h3>
    <ul class="answers">
      <li><span class="answer-label">Best Answer:</span> Super-majority.</li>
      <li>Indicates commitment, experience, and focus on NCC and overcomes dependency on buyout heritage, if any.</li>
    </ul>
  </section>

  <div class="brand">
    <span class="brand-dot"></span>
    <span class="brand-name">RIDGEHOLM</span>
  </div>
</div>
</body>
</html>
```